Design my site www.briefmarkpost.com

So here is what I am thinking in terms of design:

https://plenvo.com

https://www.skylarkjetways.com

http://quillweekly.com/harbor-tower-plaza/

I want the theme to be white and blue (royal blue). I attached a paint picture of what I would like the site to look like in terms of placing the text. Generally, what I like about the sites above is that they are simple, you can navigate easily and have some kind of idea of what's going on by looking at the center (picture and motto). Let's establish a clear understanding of how the functional part of the site would look like. Please see the picture attached.

I want to keep it simple: On top would be the Name 'BRIEFMARK post", somewhere to the right on top on the page would be 'Sign in" button.

In the center would be a picture (maybe a video) with the Motto (on top of it all in capital) OBSERVE NAVIGATE DECIDE and below would be the "sign up now"

Below the picture (like on quillweekly.com site) or to the left on top of the page would be "About Us', "Press" "Contact Us' buttons.

Then once the user gets to his page his got 3 tabs " Press Headlines", "Events", " Briefings".

we would keep the same format I only have on the site, but separate for every Tab.

I do not want the user to get distracted. I also want him to be able to access the page though mobile phone and be able to get automatic updates just like Zentro Pings without having to sign in daily.

The landing page must be minimalist yet with business/corporate feel where users can navigate easily and a "what you see is what you get" approach. You want an image or video (personally I prefer the video.. it does capture the users attention instantly, as long as it is an interesting video), with your taglines in it.

Sections available to public: About Us, Contact Us, Landing Page with Signup Option

Private: Public Sections + User Account Page, Tabs for (Events, Press Headlines, Briefings)

Target Market(s)

PR/media monitoring/diplomatic community

Coding

Coded - Design and coding required

Number of Pages Required

1 page

Font styles to use
Serif
Sans Serif

Colors
0255a3
ec1f27

Requirements
Must have
• a simple landing page, that is user friendly.
Nice to have
• a video with the explanation of how to navigate the site
Should not have
• too many colors, graphs etc.

```html
<!DOCTYPE html>
<html lang="en">
<head>
<meta charset="utf-8">
<title>BRIEFMARK post</title>
<link rel="stylesheet" href="https://fonts.googleapis.com/css2?family=Roboto:wght@400;500;700&family=Homemade+Apple&display=swap">
<style>
:root{
  --blue:#0b52ab;
  --accent:#2fa6d9;
  --ink:#222629;
  --muted:#6b7075;
  --panel:#f4f6f9;
  --footer:#30353b;
  --footer-text:#a9afb5;
  --white:#ffffff;
}
*{box-sizing:border-box;margin:0;padding:0}
html,body{width:1200px;height:2723px;overflow:hidden;background:var(--white)}
body{font-family:'Roboto',Arial,sans-serif;color:var(--ink);position:relative}

/* Header */
.site-header{position:absolute;left:0;top:0;width:1200px;height:69px;border-bottom:1px solid #e3e3e3;background:var(--white)}
.brand{position:absolute;left:51px;top:18px;font-size:28px;font-weight:700;color:var(--blue);letter-spacing:.3px;line-height:32px}
.main-nav{position:absolute;right:0;top:0;height:69px;display:flex;align-items:center}
.main-nav a{font-size:13px;color:var(--ink);text-decoration:none;margin-right:36px;text-transform:uppercase}
.main-nav .sign-in{background:var(--blue);color:var(--white);font-weight:700;height:69px;width:58px;display:flex;align-items:center;justify-content:center;margin-right:51px;font-size:12px}

/* Hero */
.hero{position:absolute;left:0;top:69px;width:1200px;height:490px;
  background:radial-gradient(ellipse 260px 330px at 230px 250px,#a99584 0%,#b8ab9e 45%,rgba(200,197,192,0) 100%),linear-gradient(90deg,#9c8f86 0%,#c6c2bd 40%,#cbc8c3 100%)}
.hero-copy{position:absolute;left:440px;top:150px;width:610px;text-align:center;color:var(--white)}
.hero-title{font-family:'Homemade Apple',cursive;font-size:60px;font-weight:400;line-height:1.2}
.hero-sub{font-size:20px;font-weight:500;margin-top:4px}
.hero-actions{margin-top:26px;display:flex;justify-content:center;gap:42px}
.btn{display:inline-flex;align-items:center;justify-content:center;height:31px;font-size:9.5px;font-weight:700;text-transform:uppercase;color:var(--white);text-decoration:none}
.btn-primary{background:var(--accent);width:94px}
.btn-ghost{border:1px solid var(--white);width:107px}

/* Section headings */
.section-title{position:absolute;left:0;width:1200px;text-align:center;font-size:22px;font-weight:700;color:var(--blue)}
.rule{position:absolute;left:51px;width:1098px;border-top:2px dotted #8fa6c4}

/* Headlines band */
.headlines{position:absolute;left:0;top:559px;width:1200px;height:374px;background:var(--blue)}
.headlines .section-title{color:var(--white);top:23px}
.headlines .rule{top:63px;left:40px;width:1122px;border-color:#b9c9e4}
.feature{position:absolute;top:105px;width:340px;text-align:center;color:var(--white)}
.feature-icon{width:76px;height:80px;margin:0 auto;background:#c9cdd3;display:flex;align-items:center;justify-content:center}
.feature h3{font-size:18px;font-weight:700;margin-top:12px}
.feature p{font-size:12.5px;line-height:22px;margin-top:14px}

/* News cards */
.card{position:absolute;top:1035px;width:254px;height:354px;background:var(--panel)}
.thumb{height:185px;position:relative}
.tone-a{background:linear-gradient(135deg,#c4ccd6,#8e9aa8)}
.tone-b{background:linear-gradient(135deg,#3b4654,#232b35)}
.tone-c{background:linear-gradient(135deg,#d4cdc3,#9c9388)}
.tone-d{background:linear-gradient(135deg,#b9c6d3,#6f8296)}
.link-badge{position:absolute;left:112px;top:78px;width:30px;height:30px;background:var(--white);border-radius:3px;display:flex;align-items:center;justify-content:center}
.card-body{padding:0 20px}
.card h4{font-size:17px;font-weight:700;margin-top:18px}
.card p{font-size:12px;line-height:18.5px;color:var(--muted);margin-top:8px;height:58px}
.card-meta{border-top:1px solid #e1e4e8;margin-top:10px;padding-top:14px;display:flex;justify-content:space-between;font-size:10px;color:var(--muted)}

/* Events */
.event{position:absolute;top:1501px;width:254px;text-align:center}
.event .thumb{height:205px}
.event h4{font-size:17px;font-weight:700;margin-top:28px}
.event p{font-size:11.5px;line-height:19px;color:var(--muted);margin-top:12px}

/* Briefing tabs */
.briefing{position:absolute;left:51px;top:1933px;width:1098px;height:354px;background:var(--panel)}
.tabs{display:flex;height:40px}
.tab{position:relative;width:156px;height:40px;display:flex;align-items:center;justify-content:center;font-size:14px;color:var(--white)}
.tab svg{position:absolute;inset:0}
.tab span{position:relative}
.tab.active{width:158px;color:var(--ink);background:var(--panel)}
.tab.last{width:160px}
.brief-item{position:absolute;left:29px;width:1040px}
.brief-thumb{position:absolute;left:0;top:0;width:132px;height:93px}
.brief-item h5{position:absolute;left:160px;top:6px;font-size:17px;font-weight:700}
.brief-item p{position:absolute;left:160px;top:32px;width:880px;font-size:12px;line-height:20px;color:var(--muted)}
.brief-divider{position:absolute;left:29px;top:198px;width:1040px;border-top:1px solid #e1e4e8}

/* Footer */
.site-footer{position:absolute;left:0;top:2303px;width:1200px;height:420px;background:var(--footer);color:var(--footer-text);font-size:12.5px;line-height:20px}
.footer-col{position:absolute;top:54px;width:254px}
.footer-col h6{font-size:16px;font-weight:400;color:var(--white);margin-bottom:24px}
.footer-col p{margin-bottom:14px}
.socials{display:flex;gap:12px;margin-top:4px}
.socials i{width:11px;height:11px;border-radius:50%;background:var(--footer-text);display:block}
.post{display:flex;align-items:center;gap:18px;margin-bottom:22px}
.post-thumb{width:46px;height:46px;border-radius:50%;flex:none}
.post b{display:block;font-weight:400;color:var(--white);font-size:12.5px}
.post small{font-size:11px}
.quote-mark{position:absolute;left:0;top:38px;font-family:Georgia,serif;font-size:78px;color:#8b9197;line-height:1}
.review-text{padding-left:48px}
.reviewer{display:flex;align-items:center;gap:20px;margin-top:4px}
.avatar{width:78px;height:78px;border-radius:50%;background:radial-gradient(circle at 50% 40%,#d8c6b4,#8d8a87);border:3px solid var(--white)}
.reviewer b{display:block;color:var(--white);font-weight:400;font-size:16px}
.footer-rule{position:absolute;left:51px;top:350px;width:1098px;border-top:1px solid #434950}
.copyright{position:absolute;left:51px;top:380px;font-size:12px}
</style>
</head>
<body>

<header class="site-header">
  <div class="brand">BRIEFMARK post</div>
  <nav class="main-nav">
    <a href="#">About Us</a>
    <a href="#">Contact Us</a>
    <a class="sign-in" href="#">Sign In</a>
  </nav>
</header>

<section class="hero" role="img" aria-label="Photo of a joyful person with raised fists against a soft grey backdrop">
  <div class="hero-copy">
    <h1 class="hero-title">Ready to Enjoy?</h1>
    <p class="hero-sub">Grab This Perfect BRIEFMARK post Now</p>
    <div class="hero-actions">
      <a class="btn btn-primary" href="#">Signup Now</a>
      <a class="btn btn-ghost" href="#">Go on Surfing</a>
    </div>
  </div>
</section>

<section class="headlines">
  <h2 class="section-title">Headlines</h2>
  <div class="rule"></div>

  <div class="feature" style="left:55px">
    <div class="feature-icon">
      <svg width="34" height="40" viewBox="0 0 34 40" fill="none" stroke="#fff" stroke-width="2"><circle cx="17" cy="15" r="10"/><circle cx="17" cy="15" r="5"/><path d="M10 23l-3 14 10-5 10 5-3-14"/></svg>
    </div>
    <h3>About Us</h3>
    <p>At vero eos et accusamus et iusto odio dignissimos ducimus qui blanditiis praesentium voluptatum deleniti atque corrupti quos dolores et quas molestias excepturi sint occaecati cupiditate non provident, similique sunt in culpa qui officia deserunt mollitiardo.</p>
  </div>
  <div class="feature" style="left:430px">
    <div class="feature-icon">
      <svg width="30" height="42" viewBox="0 0 30 42" fill="none" stroke="#fff" stroke-width="2"><path d="M15 3c6 6 7 14 5 24H10C8 17 9 9 15 3z"/><circle cx="15" cy="16" r="3"/><path d="M10 22l-5 7h6M20 22l5 7h-6M12 32l3 7 3-7"/></svg>
    </div>
    <h3>Press</h3>
    <p>At vero eos et accusamus et iusto odio dignissimos ducimus qui blanditiis praesentium voluptatum deleniti atque corrupti quos dolores et quas molestias excepturi sint occaecati cupiditate non provident, similique sunt in culpa qui officia deserunt mollitiardo.</p>
  </div>
  <div class="feature" style="left:805px">
    <div class="feature-icon">
      <svg width="30" height="40" viewBox="0 0 30 40" fill="none" stroke="#fff" stroke-width="2"><path d="M3 2h16l8 8v28H3z"/><path d="M19 2v8h8M8 17h14M8 23h14M8 29h14"/></svg>
    </div>
    <h3>Contact Us</h3>
    <p>At vero eos et accusamus et iusto odio dignissimos ducimus qui blanditiis praesentium voluptatum deleniti atque corrupti quos dolores et quas molestias excepturi sint occaecati cupiditate non provident, similique sunt in culpa qui officia deserunt mollitiardo.</p>
  </div>
</section>

<h2 class="section-title" style="top:938px">Latest News &amp; Views</h2>
<div class="rule" style="top:976px"></div>

<article class="card" style="left:51px">
  <div class="thumb tone-a" role="img" aria-label="News photo"></div>
  <div class="card-body">
    <h4>Ullamcorper Parturien</h4>
    <p>Morbi leo risus, porta ac consectetur ac eros. Maecenas sed diam eget risus varius blandit sit amet non.</p>
    <div class="card-meta"><span>&#9638; 28 October, 2020</span><span>&#9993; 15</span></div>
  </div>
</article>
<article class="card" style="left:332px">
  <div class="thumb tone-b" role="img" aria-label="News photo with link overlay">
    <span class="link-badge"><svg width="14" height="14" viewBox="0 0 14 14" fill="none" stroke="#2c3540" stroke-width="2"><path d="M6 8l2-2M5 6L3 8a2 2 0 003 3l2-2M9 8l2-2a2 2 0 00-3-3L6 5"/></svg></span>
  </div>
  <div class="card-body">
    <h4>Excepteur Sint Occaecat</h4>
    <p>Lorem ipsum dolor sit amet, consectetur adipiscing elit, sed do eiusmod tempor incididunt ut lab.</p>
    <div class="card-meta"><span>&#9638; 27 October, 2020</span><span>&#9993; 11</span></div>
  </div>
</article>
<article class="card" style="left:613px">
  <div class="thumb tone-c" role="img" aria-label="News photo"></div>
  <div class="card-body">
    <h4>Neque Porro Quisquam</h4>
    <p>Sed ut perspiciatis unde omnis iste natus error sit voluptatem accusantium doloremque laudanti.</p>
    <div class="card-meta"><span>&#9638; 26 October, 2020</span><span>&#9993; 10</span></div>
  </div>
</article>
<article class="card" style="left:895px">
  <div class="thumb tone-d" role="img" aria-label="News photo"></div>
  <div class="card-body">
    <h4>Quis Autem Vel Eum</h4>
    <p>Nemo enim ipsam voluptatem quia voluptas sit aspernatur aut odit aut fugit, sed quia consequ.</p>
    <div class="card-meta"><span>&#9638; 25 October, 2020</span><span>&#9993; 15</span></div>
  </div>
</article>

<h2 class="section-title" style="top:1405px">Events</h2>
<div class="rule" style="top:1443px"></div>

<div class="event" style="left:51px"><div class="thumb tone-d" role="img" aria-label="Event photo"></div><h4>Ultra Responsive</h4><p>Lorem ipsum dolor sit amet einem,<br>consectetur adipiscing elit, sed do in.</p></div>
<div class="event" style="left:332px"><div class="thumb tone-c" role="img" aria-label="Event photo"></div><h4>Unique Features</h4><p>Eiusmod tempor incididunt ut labore et<br>dolore magna aliqua ut enim ad.</p></div>
<div class="event" style="left:613px"><div class="thumb tone-a" role="img" aria-label="Event photo"></div><h4>Easy to Customize</h4><p>Aliquip ex ea commodo consequat. Duis<br>aute irure dolor in reprehenderit.</p></div>
<div class="event" style="left:895px"><div class="thumb tone-c" role="img" aria-label="Event photo"></div><h4>Layout Builder</h4><p>Duis aute irure dolor in reprehenderit in<br>voluptate velit esse cillum dolore.</p></div>

<h2 class="section-title" style="top:1844px">Daily Briefind</h2>
<div class="rule" style="top:1882px"></div>

<section class="briefing">
  <div class="tabs">
    <div class="tab active"><span>Strategy</span></div>
    <div class="tab"><svg width="156" height="40" viewBox="0 0 156 40"><path d="M0 0h146l10 40H0z" fill="var(--blue)"/></svg><span>Analysis</span></div>
    <div class="tab"><svg width="156" height="40" viewBox="0 0 156 40"><path d="M0 0h146l10 40H0z" fill="var(--blue)"/></svg><span>Markets</span></div>
    <div class="tab"><svg width="156" height="40" viewBox="0 0 156 40"><path d="M0 0h146l10 40H0z" fill="var(--blue)"/></svg><span>Calendars</span></div>
    <div class="tab"><svg width="156" height="40" viewBox="0 0 156 40"><path d="M0 0h146l10 40H0z" fill="var(--blue)"/></svg><span>Our View</span></div>
    <div class="tab"><svg width="156" height="40" viewBox="0 0 156 40"><path d="M0 0h146l10 40H0z" fill="var(--blue)"/></svg><span>Free Emails</span></div>
    <div class="tab last"><svg width="160" height="40" viewBox="0 0 160 40"><path d="M0 0h150l10 40H0z" fill="var(--blue)"/></svg><span>Business</span></div>
  </div>

  <div class="brief-item" style="top:76px">
    <div class="brief-thumb" role="img" aria-label="Photo of a laptop and coffee on a desk" style="background:linear-gradient(120deg,#c9c2b8,#8f8a84 55%,#d9d4cc)"></div>
    <h5>Lorem Ipsum Dolor Sit Amet</h5>
    <p>Sed ut perspiciatis unde omnis iste natus error sit voluptatem accusantium doloremque laudantium, totam rem aperiam, eaque ipsa quae ab illo inventore veritatis et quasi architecto beatae vitae dicta sunt explicabo. Nemo enim ipsam voluptatem quia volupt. Temporibus autem quibusdam et aut officiis debitis aut rerum necessitatibus saepe eveniet ut et voluptates repudiandae sint et molestiae non recusandae. Itaque earum rerum hic tenetur at.</p>
  </div>
  <div class="brief-divider"></div>
  <div class="brief-item" style="top:225px">
    <div class="brief-thumb" role="img" aria-label="Photo of a coffee maker and plant on a counter" style="background:linear-gradient(120deg,#e2e0dc,#8b8680 50%,#5f5a55)"></div>
    <h5>Sed Ut Perspiciatis Unde Omnis</h5>
    <p>Neque porro quisquam est, qui dolorem ipsum quia dolor sit amet, consectetur, adipisci velit, sed quia non numquam eius modi tempora incidunt ut labore et dolore magnam aliquam quaerat voluptatem. Ut enim ad minima veniam, quis nostrum exercitationem. Temporibus autem quibusdam et aut officiis debitis aut rerum necessitatibus saepe eveniet ut et voluptates repudiandae sint et molestiae non recusandae. Itaque earum rerum hic tenetur at.</p>
  </div>
</section>

<footer class="site-footer">
  <div class="footer-col" style="left:51px">
    <h6>Contacts</h6>
    <p>Maecenas etos sit amet, consectetur adipiscing elit. Terminal volutpat rutrum metro amet sollicitudin interdum.</p>
    <p>Phone: +1 (555) 210 48 63</p>
    <p>Office: 418 Marlow Lane, Ashford</p>
    <p>Email: info@briefmarkpost.com</p>
    <div class="socials"><i></i><i></i><i></i><i></i><i></i></div>
  </div>
  <div class="footer-col" style="left:332px">
    <h6>Recent Posts</h6>
    <div class="post"><div class="post-thumb" role="img" aria-label="Post thumbnail photo" style="background:radial-gradient(circle,#9a8a7c,#4b4642)"></div><div><b>Standard Post</b><small>Jun 22, 2015 / 0 comments</small></div></div>
    <div class="post"><div class="post-thumb" role="img" aria-label="Post thumbnail photo" style="background:radial-gradient(circle,#b8b2aa,#6c6863)"></div><div><b>Video Post</b><small>Jun 22, 2015 / 0 comments</small></div></div>
    <div class="post"><div class="post-thumb" role="img" aria-label="Post thumbnail photo" style="background:radial-gradient(circle,#a6846a,#4e3f35)"></div><div><b>Post with Image</b><small>Jun 22, 2015 / 0 comments</small></div></div>
  </div>
  <div class="footer-col" style="left:613px">
    <h6>About Team</h6>
    <p>Enim congue blandit. Lorem ipsum dolor sit amet, consectetur interdum finibus. Quisque consectetur interdum finibus. Vestibulum ante ipsum primis in faucibus orci. luctus et ultrices posuere.</p>
    <p>Cubilia cras blandit finibus ipsum, id porttitor arcu volutpat a. Integer iaculis erat nec justo malesuada faucibus vel tempus sapien. Vivamus aliquam euismod tristique.</p>
  </div>
  <div class="footer-col" style="left:895px">
    <h6>Last Review</h6>
    <span class="quote-mark">&ldquo;</span>
    <p class="review-text">At vero eos et accusamus et iusto odio dignissimos ducimus qui blanditiis praesentium voluptatum deleniti atque corrupti quos dolores et quas molestias excepturi sint occaecati.</p>
    <div class="reviewer">
      <div class="avatar" role="img" aria-label="Portrait photo of the reviewer"></div>
      <div><b>Evan Corlish</b><small>Developer</small></div>
    </div>
  </div>
  <div class="footer-rule"></div>
  <p class="copyright">Copyright &copy; 2020. All Rights Reserved</p>
</footer>

</body>
</html>
```